Tidewell HVAC WordPress website design

Design a new modern, clean, website for HVAC mechanical business that uses company logo/colors for branding and recognition. Files attached are just for band and color information. Here is a website design that appeals to me https://www.quillerbyhomes.example/

A clear description of who we are and what we do

An easily-navigated site map

An easily-navigated site map for mobile devices

Easy-to-find contact information

Obvious call to action for service, installs or to schedule estimates

about us page

Provide a way for potential customers to contact us via text or email

provide a way that allows a customer to upload a picture to request a service call or quote.
Updates

I'm looking for the design to be completed in WordPress

Industry/Entity Type

HVAC Mechanical & Building Automation / Controls contractor

Coding

Coded - Design and coding required

Number of Pages Required

5+ page

Colors
0054AA
0677BA
7BADD7
CADEEF
E8F1F8

Requirements
Must have
• Design a new modern, clean, website for HVAC mechanical business that uses company logo/colors for branding and recognition. Files attached are just for band and color information. Here is a website design that appeals to me https://www.quillerbyhomes.example/ A clear description of who we are and what we do An easily-navigated site map An easily-navigated site map for mobile devices Easy-to-find contact information Obvious call to action for service, installs or to schedule estimates about us page Provide a way for potential customers to contact us via text or email provide a way that allows a customer to upload a picture to request a service call or quote.
Nice to have

```html
<!DOCTYPE html>
<html lang="en">
<head>
<meta charset="utf-8">
<title>Tidewell HVAC</title>
<link href="https://fonts.googleapis.com/css2?family=Outfit:wght@300;400;500;600;700&display=swap" rel="stylesheet">
<style>
:root{
  --navy:#10085f;
  --blue:#1d8bd8;
  --blue-dark:#0b3f9a;
  --sky:#7badd7;
  --ice:#e8f1f8;
  --ink:#1a1a2e;
  --muted:#6b6f80;
  --stage:#1f7ad0;
  --white:#ffffff;
}
*{margin:0;padding:0;box-sizing:border-box}
html,body{width:1200px;height:2509px;overflow:hidden;background:var(--stage);font-family:'Outfit',sans-serif;color:var(--ink)}
.stage{position:absolute;left:0;top:0;width:1232px;height:2576px;transform:scale(.974);transform-origin:0 0}
.page{position:absolute;left:271px;top:116px;width:690px;height:2344px;background:var(--white);overflow:hidden;box-shadow:0 20px 60px rgba(0,0,40,.35)}
.abs{position:absolute}
.topbar{left:0;top:0;width:690px;height:26px;background:var(--navy);color:#fff;font-size:7px;font-weight:500}
.topbar span{position:absolute;top:9px}
.dot{display:inline-block;width:5px;height:5px;border-radius:50%;background:var(--blue);position:absolute;top:10px}
.nav{left:0;top:26px;width:690px;height:30px;background:#fff}
.logo{display:flex;align-items:center;gap:4px;font-weight:700;color:var(--navy);font-size:8px;white-space:nowrap}
.logo i{width:9px;height:9px;border-radius:50%;background:var(--blue);display:block}
.menu a{position:absolute;top:12px;font-size:7.5px;color:var(--ink);text-decoration:none}
.btn{background:var(--blue);color:#fff;font-size:5px;font-weight:600;display:flex;align-items:center;justify-content:center}
.hero{left:0;top:56px;width:690px;height:356px;background:linear-gradient(100deg,#14104f 0%,#2a2f70 40%,#4f6aa0 70%,#24306e 100%)}
.hero-panel{left:129px;top:110px;width:52px;height:215px;background:var(--navy)}
.eyebrow{font-size:6px;color:var(--blue);font-weight:500}
.stats{left:132px;top:384px;width:425px;height:62px;background:#fff;box-shadow:0 4px 14px rgba(0,0,0,.12)}
.stat{position:absolute;top:10px;width:95px;height:42px;border:1px solid #eef0f4}
.stat b{position:absolute;left:37px;top:7px;font-size:13px;color:var(--navy);font-weight:600}
.stat small{position:absolute;left:37px;top:27px;font-size:4px;color:var(--blue)}
.stat svg{position:absolute;left:10px;top:9px}
.h2{font-weight:600;color:var(--navy)}
.tiny{font-size:4.2px;line-height:1.55;color:var(--muted)}
.check{font-size:4.5px;color:var(--ink);display:flex;align-items:center;gap:3px;position:absolute}
.check i{width:4px;height:4px;background:var(--blue);display:block}
.work{left:129px;top:777px;width:302px;height:168px;background:var(--navy)}
.step{position:absolute;top:818px;width:79px;height:95px;background:var(--blue);color:#fff;padding:10px}
.step small{font-size:4px;display:block}
.step b{font-size:7.5px;font-weight:500;display:block;margin-top:6px}
.step hr{border:0;border-top:1px solid #fff;width:14px;margin:7px 0}
.step p{font-size:4px;line-height:1.5}
.svc{position:absolute;width:90px;text-align:center}
.svc h4{font-size:8.5px;font-weight:500;line-height:1.2;color:var(--ink)}
.pill{position:absolute;width:44px;height:22px;border-radius:50%;background:radial-gradient(ellipse at 50% 30%,#2f6fd0,#0b2d7a);border:2px solid #c8cbd6;color:#fff;font-size:5px;font-weight:600;display:flex;align-items:center;justify-content:center}
.ph{position:absolute}
.foot a{display:block;font-size:4.5px;color:#c8cdf0;margin-bottom:9.5px}
.foot h5{font-size:6px;color:#fff;font-weight:500;margin-bottom:10px}
</style>
</head>
<body>
<div class="stage">
<div class="page">

  <div class="abs topbar">
    <span style="left:132px">Calling Us</span>
    <span style="left:197px;padding-left:8px">&#9742; +123 456 789</span>
    <span style="left:265px">&#9993; hello@tidewellhvac.example</span>
    <span style="left:458px">Follow Us:</span>
    <i class="dot" style="left:516px"></i><i class="dot" style="left:530px"></i><i class="dot" style="left:544px"></i>
  </div>

  <div class="abs nav">
    <div class="abs logo" style="left:133px;top:10px"><i></i>Tidewell HVAC</div>
    <nav class="menu">
      <a class="abs" style="left:208px;color:var(--navy)">Home</a>
      <a class="abs" style="left:246px">About Us</a>
      <a class="abs" style="left:295px">Contact Us</a>
      <a class="abs" style="left:352px">Service</a>
    </nav>
    <div class="abs btn" style="left:470px;top:5px;width:85px;height:19px">Make Appointment &rarr;</div>
  </div>

  <div class="abs hero" role="img" aria-label="Photo of a smiling HVAC technician in blue overalls holding a notepad beside rooftop units"></div>
  <svg class="abs" style="left:380px;top:56px" width="310" height="356" viewBox="0 0 310 356"><path d="M40 0 Q250 20 310 120 L310 40 Q260 0 220 0Z" fill="#8d96b3" opacity=".7"/><path d="M310 250 Q270 330 170 356 L230 356 Q290 320 310 290Z" fill="#9aa2bc" opacity=".7"/></svg>
  <div class="abs hero-panel"></div>
  <div class="abs eyebrow" style="left:150px;top:152px">Trusted HVAC Service</div>
  <div class="abs" style="left:150px;top:167px;color:#fff;font-size:26px;font-weight:600;line-height:1.2">Professional<br>HVAC Service</div>
  <div class="abs" style="left:150px;top:242px;color:#dfe3f5;font-size:4.2px">Have a home repair issue? Call 24 hours emergency services all time!</div>
  <div class="abs" style="left:150px;top:259px;width:181px;height:26px;background:var(--navy)"></div>
  <div class="abs" style="left:150px;top:259px;width:30px;height:26px;background:var(--blue)">
    <svg width="30" height="26" viewBox="0 0 30 26"><path d="M10 7c1 5 4 9 9 11l2-2 3 2-2 3c-7-1-13-8-14-14l3-2 2 3z" fill="none" stroke="#fff" stroke-width="1.3"/></svg>
  </div>
  <div class="abs" style="left:189px;top:267px;color:#fff;font-size:10px;font-weight:600">Call Us Now <span style="color:var(--blue);font-weight:400">+123 456 789</span></div>

  <div class="abs stats">
    <div class="stat" style="left:10px"><svg width="22" height="22" viewBox="0 0 22 22" fill="none" stroke="#1d8bd8" stroke-width="1"><circle cx="11" cy="6" r="3"/><circle cx="4" cy="13" r="2"/><circle cx="18" cy="13" r="2"/><path d="M5 20c0-4 3-7 6-7s6 3 6 7M0 21c0-3 2-5 4-5M22 21c0-3-2-5-4-5"/></svg><b>1200+</b><small>Happy Customers</small></div>
    <div class="stat" style="left:115px"><svg width="22" height="22" viewBox="0 0 22 22" fill="none" stroke="#1d8bd8" stroke-width="1"><rect x="4" y="3" width="10" height="18"/><rect x="14" y="9" width="5" height="12"/><path d="M7 7h4M7 11h4M7 15h4"/></svg><b>35+</b><small>Branch Offices</small></div>
    <div class="stat" style="left:220px"><svg width="22" height="22" viewBox="0 0 22 22" fill="none" stroke="#1d8bd8" stroke-width="1"><circle cx="11" cy="10" r="6"/><path d="M8 10l2 2 4-4M7 15l-2 6 4-2 2 2M15 15l2 6-4-2"/></svg><b>2500+</b><small>Projects Completed</small></div>
    <div class="stat" style="left:325px"><svg width="22" height="22" viewBox="0 0 22 22" fill="none" stroke="#1d8bd8" stroke-width="1"><path d="M6 3h10v6a5 5 0 0 1-10 0zM6 5H2c0 4 2 5 4 5M16 5h4c0 4-2 5-4 5M11 14v4M7 20h8"/></svg><b>45+</b><small>Win Awards</small></div>
  </div>

  <!-- about -->
  <div class="ph" style="left:150px;top:590px;width:150px;height:78px;border-radius:50%;background:linear-gradient(#dde1ec,#9aa4bf)"></div>
  <div class="ph" style="left:156px;top:595px;width:138px;height:68px;border-radius:50%;background:linear-gradient(var(--blue),var(--blue-dark))"></div>
  <div class="ph" role="img" aria-label="Photo of an HVAC technician in overalls" style="left:176px;top:508px;width:100px;height:140px;border-radius:6px;background:linear-gradient(160deg,#a9c6e2,#3a78bd)"></div>
  <div class="abs" style="left:234px;top:638px;width:94px;height:41px;background:var(--navy);color:#fff;text-align:center">
    <div style="font-size:17px;font-weight:600;line-height:1;margin-top:5px">12+</div>
    <div style="font-size:6px">Years of Experienced</div>
  </div>
  <div class="abs eyebrow" style="left:350px;top:509px">Protecting Anything</div>
  <div class="abs h2" style="left:350px;top:522px;font-size:13.5px;line-height:1.3">We Offer The Perfect Solution<br>For Your Home Problems</div>
  <p class="abs tiny" style="left:350px;top:567px;width:210px">Lorem ipsum is simply dummy text of the printing and typesetting industry. Lorem ipsum has been the industry's standard dummy text ever since the 1500s, when an unknown printer took a galley of type and scrambled it to make a type specimen book.</p>
  <p class="abs tiny" style="left:350px;top:606px;width:210px">It has survived not only five centuries, but also the leap into electronic typesetting, remaining essentially unchanged. It was popularised in the 1960s with the release of Letraset sheets containing lorem ipsum passages, and more recently with desktop publishing software like page makers including versions of lorem ipsum.</p>
  <div class="check" style="left:350px;top:659px"><i></i>Quality Control System</div>
  <div class="check" style="left:350px;top:671px"><i></i>Satisfaction Guarantee</div>
  <div class="check" style="left:350px;top:683px"><i></i>Professional Crew</div>
  <div class="check" style="left:455px;top:659px"><i></i>Professional &amp; Qualified</div>
  <div class="check" style="left:455px;top:671px"><i></i>High Quality Design</div>
  <div class="check" style="left:455px;top:683px"><i></i>Satisfaction Guarantee</div>
  <div class="abs btn" style="left:350px;top:701px;width:63px;height:19px">More About Us</div>

  <!-- how we work -->
  <div class="abs work"></div>
  <div class="abs eyebrow" style="left:151px;top:819px">Step of Work</div>
  <div class="abs" style="left:151px;top:834px;color:#fff;font-size:13px;font-weight:600">How We Work</div>
  <p class="abs tiny" style="left:151px;top:859px;width:130px;color:#d5d9f2">Lorem ipsum dolor sit amet consectetur adipiscing elit tellus luctus ipsum a nec ullam pulvinar dapibus maecenas maximus viverra malesuada.</p>
  <div class="abs btn" style="left:151px;top:894px;width:59px;height:19px">View Services</div>
  <div class="step" style="left:305px"><small>01</small><b>Oppointment</b><hr><p>Lorem ipsum dolor sit amet consectetur adipiscing elit tellus.</p></div>
  <div class="step" style="left:392px;background:#2a93dc"><small>02</small><b>Analyse</b><hr><p>Lorem ipsum dolor sit amet consectetur adipiscing elit tellus.</p></div>
  <div class="step" style="left:478px;background:#2e97df"><small>03</small><b>Execute</b><hr><p>Lorem ipsum dolor sit amet consectetur adipiscing elit tellus.</p></div>

  <!-- services -->
  <div class="abs eyebrow" style="left:0;width:690px;text-align:center;top:1005px;padding-left:4px">Our Services</div>
  <div class="abs h2" style="left:0;width:690px;text-align:center;top:1019px;font-size:14px;color:var(--ink)">All Types Of Repair Service Provide</div>

  <svg class="abs" style="left:0;top:0" width="690" height="1340" fill="none" stroke="#1d8bd8" stroke-width="1">
    <rect x="122" y="1071" width="34" height="12"/><path d="M126 1078h26"/>
    <rect x="232" y="1060" width="16" height="24" rx="2"/><path d="M235 1068h10M235 1072h10M235 1076h10"/>
    <circle cx="339" cy="1077" r="7"/><path d="M346 1072h9v6h-6M339 1073v8M335 1077h8"/>
    <rect x="438" y="1062" width="12" height="24"/><circle cx="444" cy="1070" r="3"/><circle cx="444" cy="1079" r="3"/><rect x="452" y="1068" width="7" height="8"/>
    <rect x="542" y="1068" width="26" height="16"/><path d="M542 1072h26"/><circle cx="548" cy="1078" r="2"/><circle cx="562" cy="1078" r="2"/>
    <rect x="128" y="1218" width="12" height="24" rx="2"/><path d="M131 1224h6M131 1229h6M131 1234h6"/>
    <path d="M228 1238l4-12h16l-4 12z"/><circle cx="238" cy="1232" r="3"/>
    <path d="M336 1220h18v6h-6v14h-6v-14h-6z"/><path d="M345 1240v5"/>
    <rect x="440" y="1228" width="20" height="14" rx="2"/><path d="M445 1228v-4h10v4M446 1235h8"/>
    <path d="M543 1242v-12l12-8 12 8v12zM550 1242v-6h10v6M555 1222v-5"/>
  </svg>

  <div class="svc" style="left:94px;top:1104px"><h4>Air<br>Conditioning</h4></div>
  <div class="svc" style="left:195px;top:1104px"><h4>Heating</h4></div>
  <div class="svc" style="left:300px;top:1106px"><h4>Heat Pump,<br>Oil &amp; Gas</h4></div>
  <div class="svc" style="left:405px;top:1106px"><h4>Dutcless<br>Mini Split</h4></div>
  <div class="svc" style="left:510px;top:1106px"><h4>Control</h4></div>
  <div class="pill" style="left:117px;top:1146px">Learn More</div>
  <div class="pill" style="left:218px;top:1145px">Learn More</div>
  <div class="pill" style="left:323px;top:1146px">Learn More</div>
  <div class="pill" style="left:428px;top:1146px">Learn More</div>
  <div class="pill" style="left:533px;top:1145px">Learn More</div>

  <div class="svc" style="left:90px;top:1260px"><h4>VFD's</h4></div>
  <div class="svc" style="left:195px;top:1260px"><h4>Pumps</h4></div>
  <div class="svc" style="left:300px;top:1258px"><h4>Gat Fitting &amp;<br>Pipping</h4></div>
  <div class="svc" style="left:405px;top:1258px"><h4>Dutcless<br>Mini Split</h4></div>
  <div class="svc" style="left:510px;top:1258px"><h4>Control</h4></div>
  <div class="pill" style="left:113px;top:1297px">Learn More</div>
  <div class="pill" style="left:218px;top:1297px">Learn More</div>
  <div class="pill" style="left:323px;top:1297px">Learn More</div>
  <div class="pill" style="left:428px;top:1297px">Learn More</div>
  <div class="pill" style="left:533px;top:1297px">Learn More</div>

  <!-- quality -->
  <div class="ph" role="img" aria-label="Photo of a technician checking an outdoor air conditioning unit at sunset" style="left:0;top:1391px;width:331px;height:346px;background:linear-gradient(120deg,#b9b3a6 0%,#8b8d92 40%,#5a5f68 70%,#c6c2b8 100%)"></div>
  <div class="abs" style="left:143px;top:1542px;width:42px;height:42px;border-radius:50%;background:var(--blue)">
    <svg width="42" height="42" viewBox="0 0 42 42" fill="none" stroke="#fff" stroke-width="1.2"><circle cx="21" cy="21" r="10"/><path d="M18 16l8 5-8 5z"/></svg>
  </div>
  <div class="abs" style="left:331px;top:1428px;width:359px;height:309px;background:var(--navy)"></div>
  <div class="abs eyebrow" style="left:363px;top:1475px">Perfect Result</div>
  <div class="abs" style="left:363px;top:1488px;color:#fff;font-size:13.5px;font-weight:600;line-height:1.35">The Quality You Expect, The Service You<br>Deserve!</div>
  <p class="abs tiny" style="left:363px;top:1536px;width:280px;color:#d5d9f2">Lorem ipsum dolor sit amet consectetur adipiscing elit tellus luctus ipsum a nec ullam pulvinar dapibus maecenas maximus viverra malesuada elit tellus luctus ipsum.</p>
  <div class="abs" style="left:363px;top:1567px;width:133px;height:105px;background:var(--blue);color:#fff;padding:14px 10px">
    <svg width="16" height="16" viewBox="0 0 16 16" fill="none" stroke="#fff" stroke-width="1"><circle cx="8" cy="8" r="6"/><path d="M8 4v4l3 2"/></svg>
    <div style="font-size:8px;font-weight:500;margin-top:6px">24/7 Availability</div>
    <p style="font-size:4.2px;margin-top:6px;line-height:1.5">Viverra finibus turpis ac mauris dignissim dictum.</p>
    <div style="font-size:4.5px;margin-top:9px;font-weight:600">See More &rarr;</div>
  </div>
  <div class="abs" style="left:510px;top:1585px;width:133px;height:106px;background:#fff;padding:14px 10px">
    <svg width="16" height="16" viewBox="0 0 16 16" fill="none" stroke="#10085f" stroke-width="1"><circle cx="8" cy="6" r="3"/><path d="M3 15c0-3 2-5 5-5s5 2 5 5M5 4h6"/></svg>
    <div style="font-size:8px;font-weight:500;margin-top:6px;color:var(--navy)">Professional Team</div>
    <p class="tiny" style="margin-top:6px">Viverra finibus turpis ac mauris dignissim dictum.</p>
    <div style="font-size:4.5px;margin-top:9px;font-weight:600">See More &rarr;</div>
  </div>

  <!-- testimonials -->
  <div class="abs eyebrow" style="left:150px;top:1814px">Testimonials</div>
  <div class="abs h2" style="left:150px;top:1830px;font-size:14px;color:var(--ink)">Our Customer Say</div>
  <div class="abs" style="left:150px;top:1853px;color:#f4b400;font-size:6px;letter-spacing:1px">&#9733;&#9733;&#9733;&#9733;&#9733;</div>
  <p class="abs tiny" style="left:150px;top:1874px;width:175px">"Sed enim lectus, porttitor eu elit nec, aliquet auctor nunc. Ut in tempor ex. Aliquam aliquet rhoncus massa eget eleifend. In suscipit, sapien dignissim placerat, augue mauris luctus, sit amet rhoncus ligula tellus eu augue." Dale Renner visited us this spring. Sed enim lectus, porttitor eu elit nec, aliquet auctor nunc. Ut in tempor ex. Aliquam aliquet rhoncus massa eget eleifend. In suscipit, sapien dignissim maximus laoreet, augue libero maximus nisl, sit amet rhoncus ligula tellus eu augue.</p>
  <div class="abs" style="left:153px;top:1955px;width:18px;height:18px;border-radius:50%;background:#c9d3e3"></div>
  <div class="abs" style="left:182px;top:1957px;font-size:6px;font-weight:500">Dale Renner</div>
  <div class="abs" style="left:182px;top:1966px;font-size:4.5px;color:var(--muted)">Client</div>
  <div class="abs" style="left:239px;top:1988px;width:3px;height:3px;border-radius:50%;background:var(--navy)"></div>
  <div class="abs" style="left:245px;top:1988px;width:3px;height:3px;border-radius:50%;background:#c8cbd6"></div>
  <div class="abs" style="left:370px;top:1812px;width:180px;height:175px;background:var(--navy)"></div>
  <div class="ph" role="img" aria-label="Photo of a smiling worker in navy coveralls" style="left:390px;top:1812px;width:140px;height:175px;background:linear-gradient(180deg,#2c3d86,#182864)"></div>
  <div class="abs" style="left:370px;top:1812px;width:38px;height:38px;background:var(--blue);color:#fff;font-size:22px;font-weight:300;text-align:center;line-height:38px">99</div>

  <!-- emergency + footer -->
  <div class="abs" style="left:0;top:2101px;width:690px;height:243px;background:var(--navy)"></div>
  <div class="abs" style="left:129px;top:2037px;width:431px;height:128px;background:var(--navy)"></div>
  <div class="abs eyebrow" style="left:165px;top:2057px">Emergency Need Help</div>
  <div class="abs" style="left:165px;top:2072px;color:#fff;font-size:13.5px;font-weight:600;line-height:1.35">Call 24 Hours Emergency<br>Services All Time!</div>
  <div class="abs btn" style="left:165px;top:2126px;width:70px;height:19px">Request a Service</div>
  <svg class="abs" style="left:243px;top:2127px" width="18" height="18" viewBox="0 0 18 18" fill="none" stroke="#1d8bd8" stroke-width="1"><path d="M4 3c1 6 5 10 11 11l1-3-3-2-2 2c-2-1-4-3-5-5l2-2-2-3z"/></svg>
  <div class="abs" style="left:267px;top:2129px;color:#fff;font-size:10px;font-weight:500">+123 456 789</div>
  <div class="ph" style="left:382px;top:2098px;width:146px;height:62px;border-radius:50%;background:linear-gradient(#dde1ec,#9aa4bf)"></div>
  <div class="ph" style="left:388px;top:2102px;width:134px;height:54px;border-radius:50%;background:linear-gradient(var(--blue),var(--blue-dark))"></div>
  <div class="ph" role="img" aria-label="Photo of an HVAC technician in overalls" style="left:414px;top:2030px;width:82px;height:110px;border-radius:6px;background:linear-gradient(160deg,#a9c6e2,#3a78bd)"></div>

  <div class="abs logo" style="left:133px;top:2206px;color:#fff"><i></i>Tidewell HVAC</div>
  <p class="abs" style="left:132px;top:2234px;width:82px;font-size:4.5px;line-height:1.6;color:#c8cdf0">Lorem ipsum dolor sit amet, consectetur adipiscing elit, sed do eiusmod tempor incididunt ut labore et dolore.</p>
  <div class="abs" style="left:132px;top:2275px;display:flex;gap:7px">
    <i style="width:11px;height:11px;background:var(--blue);display:block"></i><i style="width:11px;height:11px;background:var(--blue);display:block"></i><i style="width:11px;height:11px;background:var(--blue);display:block"></i><i style="width:11px;height:11px;background:var(--blue);display:block"></i>
  </div>
  <div class="abs foot" style="left:240px;top:2196px"><h5>Explore Us</h5><a>&rsaquo; About Us</a><a>&rsaquo; How It Works</a><a>&rsaquo; Terms &amp; Conditions</a><a>&rsaquo; News &amp; Articles</a><a>&rsaquo; Contact Us</a></div>
  <div class="abs foot" style="left:348px;top:2196px"><h5>Services</h5><a>&rsaquo; Air Conditioning</a><a>&rsaquo; Heating</a><a>&rsaquo; Heat Pumps / Gas / Oil</a><a>&rsaquo; Ductless Mini Splits</a><a>&rsaquo; Controls</a></div>
  <div class="abs foot" style="left:456px;top:2196px"><h5>&nbsp;</h5><a>&rsaquo; VFD's</a><a>&rsaquo; Pumps</a><a>&rsaquo; Gas Fitting / Piping</a><a>&rsaquo; Service &amp; New Install</a><a>&rsaquo; Residential / Commercial</a></div>
  <div class="abs" style="left:132px;top:2310px;width:425px;border-top:1px solid #2c2680"></div>
  <div class="abs" style="left:0;top:2323px;width:690px;text-align:center;font-size:4.5px;color:#fff">&copy; Copyright 2024 By Tidewell HVAC</div>

</div>
</div>
</body>
</html>
```